Relationship Seminar

I am an Author and Speaker and I need a flyer for a Christian relationship seminar targeting women aged between mid 20's to late 30's. It's an event for women only.

-I am looking for a fresh/ edgy look but still feminine
-Nothing too girly
-Maximum of 3 colours (Spring colours are good)
-I want the flyer to convey joy or happiness
-Use my photo which is attached as the predominant image (you can crop it to remove the background etc)

The Flyer Details are as follows:

Somewhere Along The Way - Brisbane Tour

Join Author & Speaker, Rosalind Kupferle, as she speaks about her new book entitled 'Somewhere Along The Way'.

Be inspired and encouraged to embrace the life that God has given you and make the most of it!

Date: Saturday 9th November 2013
Time: 2:00 pm - 5:00 pm
Location: Harwick Lodge Brisbane (Juniper Hall)
Pelham Crescent, Brisbane QLD 4000
Tickets: $60/pp (Includes High Tea)
Buy Tickets: www.rosalindkupferle.com or http://somewherealongtheway.ticketquarry.net

Email: info@rosalindkupferle.com

Include the cover of my new book.

www.rosalindkupferle.com (include my website at the bottom of the flyer)

Target Market(s)

Young professional women aged between their mid 20's to late 30's

Industry/Entity Type

Event

Requirements
Should not have
• -No girly or curly font

```html
<!DOCTYPE html>
<html lang="en">
<head>
<meta charset="utf-8">
<title>Somewhere Along The Way – Brisbane Tour</title>
<link rel="stylesheet" href="https://fonts.googleapis.com/css2?family=Lobster&family=Lobster+Two:ital,wght@1,700&family=Sansita:ital,wght@0,700;1,700&display=swap">
<style>
  :root {
    --paper: #ffffff;
    --crimson: #a51c2e;
    --scarlet: #d8262a;
    --tangerine: #ea7a1e;
    --apricot: #f0b35a;
    --ochre: #d6a03a;
    --cover-top: #f3efe9;
    --cover-bottom: #e3e6df;
    --portrait-dark: #2a1f1d;
    --portrait-warm: #7a4a36;
  }
  * { margin: 0; padding: 0; box-sizing: border-box; }
  html, body { width: 910px; height: 1200px; overflow: hidden; background: var(--paper); }
  .flyer { position: relative; width: 910px; height: 1200px; overflow: hidden; background: var(--paper); }

  .book-cover {
    position: absolute; left: 440px; top: -20px; width: 470px; height: 750px;
    transform: rotate(5deg); transform-origin: top left;
    background: linear-gradient(180deg, var(--cover-top), var(--cover-bottom));
    box-shadow: 0 0 18px rgba(0,0,0,.12);
    opacity: .75;
  }
  .portrait {
    position: absolute; left: 450px; top: 520px; width: 460px; height: 680px;
    border-radius: 48% 0 0 0 / 30% 0 0 0;
    background: radial-gradient(ellipse at 40% 35%, var(--portrait-warm) 0 30%, var(--portrait-dark) 75%);
  }

  .title, .tagline, .intro, .details, .tickets { position: absolute; left: 0; }
  .title { font-family: "Lobster", cursive; line-height: 1; }
  .title-main { position: absolute; left: 8px; top: 10px; font-size: 70px; color: var(--crimson); white-space: nowrap; }
  .title-tour { position: absolute; left: 195px; top: 95px; font-size: 74px; color: var(--scarlet); white-space: nowrap; }

  .tagline {
    left: 32px; top: 200px; font-family: "Lobster Two", cursive; font-style: italic; font-weight: 700;
    font-size: 30px; line-height: 47px; color: var(--scarlet);
  }
  .intro {
    left: 32px; top: 330px; font-family: "Lobster Two", cursive; font-style: italic; font-weight: 700;
    font-size: 27px; line-height: 52px; color: var(--tangerine);
  }
  .intro .speaker { font-family: "Lobster", cursive; font-style: normal; font-weight: 400; font-size: 40px; }
  .intro .book-title { font-size: 30px; }

  .details { left: 32px; top: 612px; font-family: "Sansita", sans-serif; font-style: italic; font-weight: 700; color: var(--apricot); }
  .details p { font-size: 30px; line-height: 38px; }
  .details .gap { margin-bottom: 56px; }
  .details .address { font-size: 20px; line-height: 26px; }

  .tickets { left: 32px; top: 1000px; font-family: "Sansita", sans-serif; font-style: italic; font-weight: 700; font-size: 21px; line-height: 30px; color: var(--ochre); }
  .tickets .email { margin-top: 34px; }
</style>
</head>
<body>
<main class="flyer">
  <div class="book-cover" role="img" aria-label="Cover of the book Somewhere Along The Way, showing a smiling couple"></div>
  <div class="portrait" role="img" aria-label="Portrait photo of author Rosalind Kupferle smiling, in a black leather jacket"></div>

  <h1 class="title">
    <span class="title-main">Somewhere Along The Way</span>
    <span class="title-tour">Brisbane Tour</span>
  </h1>

  <p class="tagline">Be inspired and encouraged to embrace the life<br>that God has given you and make the most of it!</p>

  <p class="intro">Join Author &amp; Speaker <span class="speaker">Rosalind Kupferle</span><br>as she speaks about her new book entitled<br><span class="book-title">‘Somewhere Along The Way’</span></p>

  <section class="details">
    <p class="gap">Date: Sat, 9th Nov 2013</p>
    <p class="gap">Time: 2:00-5:00 pm</p>
    <p>Location: Juniper Hall,</p>
    <p>Harwick Lodge Brisbane</p>
    <p class="address">Pelham Crescent, Brisbane QLD 4000</p>
  </section>

  <section class="tickets">
    <p>Tickets: $60/pp (includes High Tea)</p>
    <p>Buy Tickets: www.rosalindkupferle.com</p>
    <p>or http://somewherealongtheway.ticketquarry.net</p>
    <p class="email">Email: info@rosalindkupferle.com</p>
  </section>
</main>
</body>
</html>
```